Introduction:
We are an Australia-based Cyber Security Penetration testing company seeking a website redesign to showcase our services, expertise, and experience. Our target audience includes businesses and organizations of all sizes who are seeking to secure their IT infrastructure against cyber threats. The purpose of the website redesign is to increase our online presence, generate leads, and establish our company as a trusted authority in the industry.
Objectives:
Create a professional and modern website that is easy to navigate and user-friendly.
Provide information about our company, services, and expertise.
Clearly display table of our 3 services: Bug Bounty as a Service, Penetration Testing and Code Review.
Generate leads through online contact forms and calls-to-action.
Optimize the website for search engines to increase visibility and traffic.
Website similar to: https://www.velmoro.com.au/.
Target Audience:
Our target audience includes businesses and organizations of all sizes that require cybersecurity penetration testing services. These include:
Small and medium-sized enterprises (SMEs)
Australian Government agencies
Design Requirements:
Clean, modern, and professional design.
Use of colors that convey trust, reliability, and expertise (such as orange and grey).
Calls-to-action that encourage visitors to contact us or request a quote.
Integration with social media channels to increase engagement and brand awareness.
A blog section to showcase our thought leadership and expertise.
A news section to share updates about our company and the industry.
Content Requirements:
Home page that introduces our company and services and highlights our expertise.
About Us page that provides information about our company, team, and values.
Services page that lists our services and explains the benefits of each.
Case Studies page that showcases our previous work and success stories.
Contact Us page that includes a contact form, phone number, and email address.
Blog section with articles related to the cybersecurity industry and our services.
News section with updates about our company and the industry.

```html
<!DOCTYPE html>
<html lang="en">
<head>
<meta charset="utf-8">
<title>Emberlayn — Cyber Security Penetration Testing</title>
<link href="https://fonts.googleapis.com/css2?family=Rajdhani:wght@600;700&family=Roboto:wght@400;500;700&display=swap" rel="stylesheet">
<style>
:root{
  --orange:#ef6a3c;
  --ink:#111111;
  --grey:#58595b;
  --muted:#8a8a8a;
  --line:#d9d9d9;
  --dark:#2b2b2b;
  --black:#0d0d0d;
  --white:#ffffff;
}
*{margin:0;padding:0;box-sizing:border-box}
html,body{width:1200px;height:4292px;overflow:hidden}
body{position:relative;background:var(--white);font-family:'Roboto',Arial,sans-serif;color:var(--ink)}
.abs{position:absolute}
.head-font{font-family:'Rajdhani','Arial Narrow',sans-serif;font-weight:700}
.top-rule{left:0;top:0;width:1200px;height:7px;background:var(--grey)}
.site-header{left:0;top:7px;width:1200px;height:126px;background:var(--white)}
.brand{display:flex;align-items:center;gap:12px;font-family:'Rajdhani',sans-serif;font-weight:700;color:var(--orange);white-space:nowrap}
.brand-dot{border-radius:50%;background:var(--orange)}
.call{left:760px;top:26px;display:flex;align-items:center;gap:10px}
.call-icon{width:34px;height:34px;border-radius:50%;background:var(--orange);display:flex;align-items:center;justify-content:center}
.call-text{font-size:11px;font-weight:700;line-height:15px}
.btn{background:var(--orange);color:var(--white);font-weight:500;display:flex;align-items:center;justify-content:center;white-space:nowrap}
.quote-top{left:903px;top:20px;width:147px;height:42px;font-size:13px}
.nav{left:0;top:92px;width:1200px;font-size:16px;font-weight:500;color:#333}
.nav span{position:absolute;white-space:nowrap}
.nav .active{color:var(--orange)}
.hero{left:0;top:133px;width:1200px;height:597px;background:linear-gradient(100deg,#050607 0%,#0e1418 35%,#1f3a46 60%,#2d3f4a 80%,#6d7d86 100%)}
.hero h1{left:130px;font-size:46px;line-height:53px;color:var(--white);white-space:nowrap}
.hero p{left:130px;font-size:17px;line-height:23px;font-weight:700;color:var(--white);white-space:nowrap}
.hero .btn{left:130px;width:172px;height:42px;font-size:15px}
.sec-title{left:0;width:1200px;text-align:center;font-size:54px;color:var(--ink)}
.sec-lede{left:270px;width:660px;text-align:center;font-size:13px;line-height:17px;color:var(--muted)}
.card{width:277px;height:390px;background:var(--white);box-shadow:0 2px 10px rgba(0,0,0,.10);top:965px}
.card-img{position:absolute;left:0;top:0;width:277px;height:187px}
.card h3{position:absolute;left:29px;top:220px;font-size:22px;line-height:21px;color:#222}
.card p{position:absolute;left:29px;top:275px;width:230px;font-size:11px;line-height:17px;color:var(--muted)}
.card .more{position:absolute;right:0;bottom:0;width:125px;height:34px;background:var(--orange);color:var(--white);font-size:15px;font-weight:700;display:flex;align-items:center;justify-content:center;padding-left:14px;clip-path:polygon(18px 0,100% 0,100% 100%,0 100%)}
.about-img{left:0;top:1542px;width:812px;height:555px;background:linear-gradient(115deg,#2a3d6a 0%,#1a1e34 40%,#2b1f33 70%,#15121c 100%)}
.about-box{left:632px;top:1693px;width:568px;height:454px;background:var(--orange)}
.about-box h2{position:absolute;left:65px;top:70px;font-size:52px;color:var(--white)}
.about-box p{position:absolute;left:65px;top:146px;width:395px;font-size:13.5px;line-height:18px;color:var(--white)}
.about-box .btn{position:absolute;left:80px;top:330px;width:128px;height:40px;background:var(--grey);font-size:14px}
.exp-box{top:2445px;width:139px;height:155px;border:2px solid #dcdcdc;text-align:center;font-size:15px;line-height:21px;color:#333}
.exp-box svg{position:absolute;left:44px;top:26px}
.exp-box span{position:absolute;left:0;right:0;top:94px}
.touch{left:0;top:2717px;width:1200px;height:550px;background:linear-gradient(180deg,#262626 0%,#3a3a3a 45%,#1f1f1f 100%)}
.touch h2{left:0;width:1200px;top:90px;text-align:center;font-size:54px;color:var(--white)}
.touch .sec-lede{top:162px;color:#cfcfcf}
.field{background:var(--white);font-size:10px;color:#888;padding:12px 12px;letter-spacing:.3px}
.touch .btn{left:530px;top:391px;width:140px;height:50px;font-size:15px;font-weight:700}
.post{top:3513px;width:430px;height:287px;background:var(--white);box-shadow:0 2px 12px rgba(0,0,0,.10)}
.post .date{position:absolute;left:38px;top:43px;font-size:15px;font-weight:700;color:var(--orange)}
.post h3{position:absolute;left:38px;top:75px;width:365px;font-family:'Rajdhani',sans-serif;font-weight:700;font-size:23px;line-height:28px;color:#222}
.post p{position:absolute;left:38px;top:140px;width:360px;font-size:12px;line-height:17px;color:var(--muted)}
.post .read{position:absolute;left:38px;top:240px;font-size:15px;font-weight:700;color:var(--orange)}
.footer{left:0;top:3917px;width:1200px;height:375px;background:var(--black);color:var(--white)}
.contact-panel{left:775px;top:3893px;width:275px;height:399px;background:var(--orange);color:var(--white)}
.foot-h{font-family:'Rajdhani',sans-serif;font-weight:700;font-size:24px}
.foot-list{font-size:12px;line-height:25px;white-space:nowrap}
.ci{display:flex;gap:10px;align-items:flex-start;font-size:12px;line-height:16px;white-space:nowrap}
.ci-icon{width:34px;height:34px;border:2px solid var(--white);border-radius:50%;flex:none;display:flex;align-items:center;justify-content:center}
</style>
</head>
<body>

<div class="abs top-rule"></div>

<header class="abs site-header">
  <div class="abs brand" style="left:150px;top:38px;font-size:40px">
    <span class="brand-dot" style="width:26px;height:26px"></span>Emberlayn
  </div>
  <div class="abs call">
    <span class="call-icon"><svg width="16" height="16" viewBox="0 0 24 24"><path fill="#fff" d="M6.6 10.8a15 15 0 0 0 6.6 6.6l2.2-2.2c.3-.3.7-.4 1-.2 1.1.4 2.3.6 3.6.6.6 0 1 .4 1 1V20c0 .6-.4 1-1 1A17 17 0 0 1 3 4c0-.6.4-1 1-1h3.5c.6 0 1 .4 1 1 0 1.3.2 2.5.6 3.6.1.3 0 .7-.2 1z"/></svg></span>
    <span class="call-text">Call Us<br>555-014-2290</span>
  </div>
  <div class="abs btn quote-top">Request a Quote</div>
  <nav class="abs nav">
    <span class="active" style="left:404px">Home</span>
    <span style="left:483px">About Us</span>
    <span style="left:586px">Services</span>
    <span style="left:684px">Case Studies</span>
    <span style="left:816px">Contact Us</span>
    <span style="left:933px">Blog</span>
    <span style="left:1005px">News</span>
  </nav>
</header>

<section class="abs hero" role="img" aria-label="Engineer working on a laptop in a server room">
  <h1 class="abs head-font" style="top:157px">Cyber Security<br>Penetration testing</h1>
  <p class="abs" style="top:277px">Lorem ipsum dolor sit amet, cons ectetur<br>adipiscinpsum dolor sit ame do.</p>
  <div class="abs btn" style="top:352px">Request a Quote</div>
</section>

<h2 class="abs sec-title head-font" style="top:800px">Our Services</h2>
<p class="abs sec-lede" style="top:879px">Lorem ipsum dolor sit amet, consectetur adipiscing elit, sed do eiusmod tempor incididunt ut labore et dolore magna aliqua. Quis ipsum suspendisse ultrices gravida. Risus commodo viverra mae</p>

<article class="abs card" style="left:150px">
  <div class="card-img" role="img" aria-label="Bug under a magnifying glass on a circuit board" style="background:linear-gradient(135deg,#5a1410,#c8321f 50%,#3a0c0a)"></div>
  <h3 class="head-font">Bug Bounty as<br>a Service</h3>
  <p>Lorem ipsum dolor sit amet, consectetur adipiscing elit, sed do eiusmod tempor incididunt ut labore et dolore ma.</p>
  <div class="more">Read More</div>
</article>
<article class="abs card" style="left:462px">
  <div class="card-img" role="img" aria-label="Digital security shield above a tablet" style="background:linear-gradient(160deg,#0b1a2e,#1f5f9a 50%,#0a1524)"></div>
  <h3 class="head-font">Penetration Testing</h3>
  <p>Lorem ipsum dolor sit amet, consectetur adipiscing elit, sed do eiusmod tempor incididunt ut labore et dolore ma.</p>
  <div class="more">Read More</div>
</article>
<article class="abs card" style="left:772px">
  <div class="card-img" role="img" aria-label="Hands typing code on a laptop" style="background:linear-gradient(135deg,#1b2340,#4a3a6a 50%,#121624)"></div>
  <h3 class="head-font">Code Review</h3>
  <p>Lorem ipsum dolor sit amet, consectetur adipiscing elit, sed do eiusmod tempor incididunt ut labore et dolore ma.</p>
  <div class="more">Read More</div>
</article>

<div class="abs about-img" role="img" aria-label="Hands on a laptop keyboard with a login padlock overlay"></div>
<section class="abs about-box">
  <h2 class="head-font">About Us</h2>
  <p>Lorem ipsum dolor sit amet, consectetur adipiscing elised do eiusmLorem ipsum dolor sit amet, consectetur adipisci ng elit, sed do eiusmod tempor incididunt ut labore et dolore magna aliqua. Ut enim ad minim veniam, quis nostruloed exercitation ullamco laboris nisi ut aliquip ex ea commodo consequat. Duis aute irure dolor in reprehenderit in voluptate velit esseod tempor incididunt ut labore et dolore magna aliqua. Ut enim ad minim veniaquis nostrud exercitation ullamco laboris nisi ut aliquip ex ea.</p>
  <div class="btn">Read More</div>
</section>

<h2 class="abs sec-title head-font" style="top:2276px">We Expertise</h2>
<p class="abs sec-lede" style="top:2355px">Lorem ipsum dolor sit amet, consectetur adipiscing elit, sed do eiusmod tempor incididunt ut labore et dolore magna aliqua. Quis ipsum suspendisse ultrices gravida. Risus commodo viverra mae</p>

<div class="abs exp-box" style="left:150px">
  <svg width="50" height="50" viewBox="0 0 50 50" fill="none" stroke="#ef6a3c" stroke-width="2"><rect x="6" y="8" width="38" height="8"/><rect x="9" y="16" width="32" height="28"/><rect x="14" y="24" width="8" height="20"/><rect x="27" y="24" width="10" height="9"/></svg>
  <span>Retail &amp;<br>Ecommerce</span>
</div>
<div class="abs exp-box" style="left:302px">
  <svg width="50" height="50" viewBox="0 0 50 50" fill="none" stroke="#ef6a3c" stroke-width="2"><path d="M4 44h42"/><rect x="8" y="32" width="6" height="12"/><rect x="18" y="26" width="6" height="18"/><rect x="28" y="20" width="6" height="24"/><rect x="38" y="14" width="6" height="30"/><path d="M8 26l12-8 8 4 10-10"/><circle cx="40" cy="8" r="5"/></svg>
  <span>Finance</span>
</div>
<div class="abs exp-box" style="left:454px">
  <svg width="50" height="50" viewBox="0 0 50 50" fill="none" stroke="#ef6a3c" stroke-width="2"><path d="M25 4v12M25 4h9v5h-9"/><path d="M8 24l17-8 17 8z"/><rect x="10" y="24" width="30" height="16"/><path d="M16 28v8M22 28v8M28 28v8M34 28v8M5 44h40"/></svg>
  <span>Government</span>
</div>
<div class="abs exp-box" style="left:606px">
  <svg width="50" height="50" viewBox="0 0 50 50" fill="none" stroke="#ef6a3c" stroke-width="2"><path d="M25 30S12 22 12 14a6 6 0 0 1 13-2 6 6 0 0 1 13 2c0 8-13 16-13 16z"/><path d="M20 16h10M25 11v10"/><path d="M4 30l10 12h8M46 30l-10 12h-8"/></svg>
  <span>Healthcare</span>
</div>
<div class="abs exp-box" style="left:758px">
  <svg width="50" height="50" viewBox="0 0 50 50" fill="none" stroke="#ef6a3c" stroke-width="2"><rect x="8" y="12" width="34" height="24"/><path d="M3 40h44"/><circle cx="25" cy="24" r="6"/><circle cx="38" cy="8" r="4"/></svg>
  <span>Technology</span>
</div>
<div class="abs exp-box" style="left:910px">
  <svg width="50" height="50" viewBox="0 0 50 50" fill="none" stroke="#ef6a3c" stroke-width="2"><path d="M10 4v10M16 4v10M7 14h12v6a6 6 0 0 1-12 0zM13 26v18"/><path d="M22 32l12-10 12 10v12H22z"/><path d="M35 28l-3 6h5l-3 6"/></svg>
  <span>Utilities and<br>Energy</span>
</div>

<section class="abs touch" role="img" aria-label="Night city skyline with network connection lines">
  <h2 class="abs head-font">Get in Touch</h2>
  <p class="abs sec-lede">Lorem ipsum dolor sit amet, consectetur adipiscing elit, sed do eiusmod tempor incididunt ut labore et dolore magna aliqua. Quis ipsum suspendisse ultrices gravida.</p>
  <div class="abs field" style="left:247px;top:241px;width:221px;height:37px">NAME</div>
  <div class="abs field" style="left:482px;top:241px;width:225px;height:37px">PHONE</div>
  <div class="abs field" style="left:723px;top:241px;width:230px;height:37px">EMAIL</div>
  <div class="abs field" style="left:247px;top:300px;width:706px;height:113px">MESSAGE</div>
  <div class="abs btn">SUBMIT</div>
</section>

<h2 class="abs sec-title head-font" style="top:3348px">Featured Posts</h2>
<p class="abs sec-lede" style="top:3427px">Lorem ipsum dolor sit amet, consectetur adipiscing elit, sed do eiusmod tempor incididunt ut labore et dolore magna aliqua. Quis ipsum suspendisse ultrices gravida. Risus commodo viverra mae</p>

<article class="abs post" style="left:150px">
  <div class="date">08 February - Blog</div>
  <h3>Lorem ipsum dolor sit amet, consect etur adipiscing elit, sed do</h3>
  <p>Lorem ipsum dolor sit amet, consectetur adipiscing elit, sed do eiusmod tempor incididunt ut labore et dolore magna aliquauis ipsum isus commodo viverra mae</p>
  <div class="read">Read More</div>
</article>
<article class="abs post" style="left:618px">
  <div class="date">08 February - Blog</div>
  <h3>Lorem ipsum dolor sit amet, consect etur adipiscing elit, sed do</h3>
  <p>Lorem ipsum dolor sit amet, consectetur adipiscing elit, sed do eiusmod tempor incididunt ut labore et dolore magna aliquauis ipsum isus commodo viverra mae</p>
  <div class="read">Read More</div>
</article>

<footer class="abs footer">
  <div class="abs brand" style="left:150px;top:135px;font-size:44px">
    <span class="brand-dot" style="width:26px;height:26px"></span>Emberlayn
  </div>
  <div class="abs" style="left:163px;top:248px;font-size:12px;white-space:nowrap">Copyright © 2023 All rights reserved.</div>

  <div class="abs foot-h" style="left:452px;top:72px">Links</div>
  <div class="abs foot-list" style="left:457px;top:116px">Home<br>About Us<br>Services<br>Case Studies<br>Contact Us<br>Blog<br>News</div>

  <div class="abs foot-h" style="left:583px;top:72px">Services</div>
  <div class="abs foot-list" style="left:588px;top:116px">Bug Bounty as a Service<br>Penetration Testing<br>Code Review.</div>

  <div class="abs foot-h" style="left:583px;top:212px">Connect</div>
  <div class="abs" style="left:586px;top:252px;display:flex;gap:20px" aria-label="Social channels">
    <span style="width:16px;height:16px;border:2px solid #fff;border-radius:50%"></span>
    <span style="width:16px;height:16px;border:2px solid #fff;border-radius:50%"></span>
    <span style="width:16px;height:16px;border:2px solid #fff;border-radius:50%"></span>
  </div>
</footer>

<section class="abs contact-panel">
  <div class="abs foot-h" style="left:47px;top:74px;font-size:28px">Contact</div>
  <div class="abs ci" style="left:47px;top:133px">
    <span class="ci-icon"><svg width="14" height="16" viewBox="0 0 24 28"><path fill="none" stroke="#fff" stroke-width="2.5" d="M12 26S3 16 3 10a9 9 0 0 1 18 0c0 6-9 16-9 16z"/><circle cx="12" cy="10" r="3" fill="#fff"/></svg></span>
    <span>Address: 42 Harbour Lane<br>Lorem ipsum dumys</span>
  </div>
  <div class="abs ci" style="left:47px;top:185px">
    <span class="ci-icon"><svg width="14" height="14" viewBox="0 0 24 24"><path fill="#fff" d="M6.6 10.8a15 15 0 0 0 6.6 6.6l2.2-2.2c.3-.3.7-.4 1-.2 1.1.4 2.3.6 3.6.6.6 0 1 .4 1 1V20c0 .6-.4 1-1 1A17 17 0 0 1 3 4c0-.6.4-1 1-1h3.5c.6 0 1 .4 1 1 0 1.3.2 2.5.6 3.6.1.3 0 .7-.2 1z"/></svg></span>
    <span>Phone:<br>(09) 555 018 342</span>
  </div>
  <div class="abs ci" style="left:47px;top:239px">
    <span class="ci-icon"><svg width="16" height="12" viewBox="0 0 24 18"><rect x="1" y="1" width="22" height="16" fill="none" stroke="#fff" stroke-width="2"/><path d="M1 1l11 9 11-9" fill="none" stroke="#fff" stroke-width="2"/></svg></span>
    <span>Email:<br>hello@emberlayn.com</span>
  </div>
</section>

</body>
</html>
```